Bail Bond post card mailer.

CourtKeyNexus.com sells

1. Direct guaranteed leads to bail bond agents
2. Website creation
3. Website SEO / MOBILE review
4. Back Links from our network of bailbond / jail websites

Our target customer is a bail bond company either big or small...

Our MAIN GOAL is to get more customers that want LEADS, yet we do offer the services.

We're wanting to do a post card mailer, that depicts the ever changing landscape of marketing. For instance phone books are not very relevant anymore, nor are phone booths etc. Times are changing and it requires changes how to attract customers online.

We're wanting the "call to action" on the post card to be directing the user to a specific URL, where they will enter their promotional code. ( We're not sure if the promotional code will be a sticker or on the address label ) We're open to thoughts on this:

We'll want to also have an leads@courtkeynexus.com and a phone number for bail bond agents to contact us.

Feel Free to visit courtkeynexus.com to take a look at the core website

```html
<!DOCTYPE html>
<html lang="en">
<head>
<meta charset="utf-8">
<title>CourtKey Nexus – Postcard</title>
<link rel="stylesheet" href="https://fonts.googleapis.com/css2?family=Montserrat:wght@300;700&family=Arimo:wght@700&display=swap">
<style>
  :root {
    --page-bg: #f3f3f3;
    --panel-blue: #0c4884;
    --panel-edge: #6e8fb6;
    --text-light: #ffffff;
    --guide-line: rgba(255, 255, 255, 0.28);
    --map-tone: rgba(20, 40, 80, 0.22);
  }
  * { box-sizing: border-box; margin: 0; padding: 0; }
  html, body {
    width: 1200px;
    height: 982px;
    overflow: hidden;
    background: var(--page-bg);
  }
  .postcard {
    position: absolute;
    left: 52px;
    top: 91px;
    width: 1111px;
    height: 858px;
    background: var(--panel-blue);
    border: 1px solid var(--panel-edge);
    overflow: hidden;
    color: var(--text-light);
  }
  .guides {
    position: absolute;
    inset: 0;
    width: 100%;
    height: 100%;
  }
  .map-area {
    position: absolute;
    left: 45px;
    top: 461px;
    width: 606px;
    height: 386px;
    background: radial-gradient(ellipse at 50% 45%, var(--map-tone), rgba(20, 40, 80, 0) 70%);
  }
  .brand-title {
    position: absolute;
    left: 67px;
    top: 58px;
    font-family: "Montserrat", sans-serif;
    font-weight: 700;
    font-size: 60px;
    line-height: 1;
    letter-spacing: -0.5px;
    white-space: nowrap;
  }
  .brand-title .light { font-weight: 300; }
  .section-title {
    position: absolute;
    left: 67px;
    top: 183px;
    font-family: "Montserrat", sans-serif;
    font-weight: 700;
    font-size: 58px;
    line-height: 1;
  }
  .offer-text {
    position: absolute;
    left: 68px;
    top: 260px;
    width: 339px;
    font-family: "Arimo", sans-serif;
    font-weight: 700;
    font-size: 11px;
    line-height: 20.7px;
    text-align: justify;
  }
  .phone {
    position: absolute;
    left: 68px;
    top: 450px;
    font-family: "Arimo", sans-serif;
    font-weight: 700;
    font-size: 22px;
    line-height: 1.1;
    white-space: nowrap;
  }
  .promo-url {
    position: absolute;
    left: 68px;
    top: 512px;
    font-family: "Arimo", sans-serif;
    font-weight: 700;
    font-size: 20px;
    line-height: 1.1;
    white-space: nowrap;
  }
  .photo-column {
    position: absolute;
    left: 767px;
    top: 0;
    width: 344px;
    height: 858px;
    display: flex;
    flex-direction: column;
  }
  .photo { width: 100%; }
  .photo-dayroom {
    height: 270px;
    background: linear-gradient(180deg, #4f7fc0 0%, #b9c7d8 45%, #2f4a78 100%);
  }
  .photo-facility {
    height: 266px;
    background: linear-gradient(180deg, #4a88d8 0%, #9fc0e6 45%, #8a8c88 80%, #6f716e 100%);
  }
  .photo-cellblock {
    height: 322px;
    background: linear-gradient(180deg, #d7d7d5 0%, #bdbdba 55%, #8f8f8c 100%);
  }
</style>
</head>
<body>
  <main class="postcard">
    <svg class="guides" viewBox="0 0 1111 858" preserveAspectRatio="none" aria-hidden="true">
      <line x1="0" y1="0" x2="1111" y2="858" stroke="var(--guide-line)" stroke-width="1.5" stroke-dasharray="9 7"/>
      <line x1="0" y1="858" x2="1111" y2="0" stroke="var(--guide-line)" stroke-width="1.5" stroke-dasharray="9 7"/>
    </svg>

    <div class="map-area" role="img" aria-label="Faint outline map of the United States"></div>

    <h1 class="brand-title">CourtKey <span class="light">Nexus</span></h1>
    <h2 class="section-title">About</h2>
    <p class="offer-text">CourtKey Nexus sends direct, guaranteed leads to bail bond agents, big or small. Phone books fade; clients now search online. We also build websites, review SEO and mobile, and add back links from our jail network. Enter the promo code from your label at the link below, or email leads@courtkeynexus.com.</p>
    <p class="phone">Call (555) 014-2290</p>
    <p class="promo-url">http://www.courtkeynexus.com/promo</p>

    <aside class="photo-column">
      <div class="photo photo-dayroom" role="img" aria-label="Photo of inmates seated in a blue-trimmed jail day room"></div>
      <div class="photo photo-facility" role="img" aria-label="Photo of a correctional facility entrance behind a fence with flags under a blue sky"></div>
      <div class="photo photo-cellblock" role="img" aria-label="Photo of a two-tier grey jail cell block"></div>
    </aside>
  </main>
</body>
</html>
```